Business Card Design Project

I want my business cards to stand and feel timeless! I also want people to get their hands on them and freak out over how cool these are, I already have a logo i just want a very cool card design! this is for a makeup artist and maybe one day a line of cosmetics.

Target Market(s)

I want this to target women from 18 to 45

Industry/Entity Type

Business

Font styles to use
Decorative
Script

Colors

Designer to choose colors to be used in the design.

Requirements
Must have
• it must be elegante

```html
<!DOCTYPE html>
<html lang="en">
<head>
<meta charset="utf-8">
<title>Clara Rose — Makeup Artist Business Card</title>
<link href="https://fonts.googleapis.com/css2?family=Poiret+One&family=Antonio:wght@300&family=Montserrat:wght@500&display=swap" rel="stylesheet">
<style>
  :root {
    --backdrop: #ece8e3;
    --card: #ffffff;
    --ink: #111111;
    --band: #e77cb2;
    --hair: #b58a72;
    --skin: #f1e0d8;
    --skin-soft: #f7eeea;
    --lip: #efc8da;
    --palette-light: #f6e4ea;
    --palette: #ebc3d1;
    --lash: #e6e6e6;
    --powder-light: #f5e3d2;
    --powder: #e8c6a4;
    --shadow: rgba(0, 0, 0, 0.22);
  }
  * { margin: 0; padding: 0; box-sizing: border-box; }
  html, body {
    width: 1200px;
    height: 905px;
    overflow: hidden;
    background: var(--backdrop);
  }
  .canvas {
    position: relative;
    width: 1200px;
    height: 905px;
  }
  .card {
    position: absolute;
    width: 588px;
    height: 340px;
    background: var(--card);
    overflow: hidden;
    box-shadow: 0 3px 8px var(--shadow);
  }
  .card--front { left: 32px; top: 150px; }
  .card--back  { left: 571px; top: 432px; }

  /* Photo areas */
  .photo { position: absolute; }
  .photo--portrait {
    left: 250px;
    top: 0;
    width: 338px;
    height: 340px;
    background: linear-gradient(180deg, var(--hair) 0%, var(--skin) 28%, var(--skin-soft) 62%, var(--lip) 86%, var(--skin-soft) 100%);
    -webkit-mask-image: linear-gradient(90deg, transparent 0%, #000 35%);
            mask-image: linear-gradient(90deg, transparent 0%, #000 35%);
  }
  .photo--palette {
    right: 0;
    top: 0;
    width: 150px;
    height: 340px;
    background: linear-gradient(180deg, var(--palette-light) 0%, var(--palette) 100%);
    -webkit-mask-image: linear-gradient(90deg, transparent 0%, #000 40%);
            mask-image: linear-gradient(90deg, transparent 0%, #000 40%);
  }
  .photo--lashes {
    left: 305px;
    top: 48px;
    width: 100px;
    height: 62px;
    border-radius: 31px;
    background: linear-gradient(160deg, var(--lash) 0%, #f6f6f6 100%);
  }
  .photo--brush {
    left: 0;
    bottom: 0;
    width: 170px;
    height: 85px;
    border-top-right-radius: 170px 85px;
    background: linear-gradient(45deg, var(--powder) 0%, var(--powder-light) 100%);
  }
  .photo--powder {
    right: 0;
    bottom: 0;
    width: 150px;
    height: 45px;
    border-top-left-radius: 150px 45px;
    background: linear-gradient(315deg, var(--powder) 0%, var(--powder-light) 100%);
  }

  /* Wordmark */
  .wordmark {
    position: absolute;
    left: 24px;
    top: 146px;
  }
  .wordmark__name {
    font-family: "Poiret One", sans-serif;
    font-weight: 400;
    font-size: 70px;
    line-height: 1;
    letter-spacing: 0.04em;
    color: var(--ink);
    text-transform: uppercase;
    white-space: nowrap;
  }
  .wordmark__role {
    margin-top: 12px;
    margin-left: 2px;
    font-family: "Montserrat", sans-serif;
    font-weight: 500;
    font-size: 11px;
    letter-spacing: 0.62em;
    color: var(--ink);
    text-transform: uppercase;
    white-space: nowrap;
  }

  /* Address band */
  .address-band {
    position: absolute;
    left: 0;
    top: 285px;
    width: 442px;
    height: 32px;
  }
  .address-band svg { position: absolute; inset: 0; }
  .address-list {
    position: absolute;
    inset: 0;
    list-style: none;
    font-family: "Antonio", sans-serif;
    font-weight: 300;
    font-size: 24px;
    line-height: 32px;
    letter-spacing: 0.12em;
    color: var(--ink);
  }
  .address-list li { position: absolute; top: 0; }
  .address-list li:nth-child(1) { left: 24px; }
  .address-list li:nth-child(2) { left: 163px; }
  .address-list li:nth-child(3) { left: 311px; }
</style>
</head>
<body>
<main class="canvas">

  <section class="card card--front" aria-label="Card front">
    <div class="photo photo--portrait" role="img" aria-label="Beauty portrait photograph with blue eye makeup and pink gloss lips"></div>
    <div class="wordmark">
      <p class="wordmark__name">Clara Rose</p>
      <p class="wordmark__role">Makeup by</p>
    </div>
    <div class="address-band">
      <svg width="442" height="32" viewBox="0 0 442 32" aria-hidden="true">
        <polygon points="0,0 422,0 442,32 0,32" fill="var(--band)"/>
      </svg>
      <ul class="address-list">
        <li>ADDRESS</li>
        <li>ADDRESS</li>
        <li>ADDRESS</li>
      </ul>
    </div>
  </section>

  <section class="card card--back" aria-label="Card back">
    <div class="photo photo--lashes" role="img" aria-label="Photograph of false eyelashes"></div>
    <div class="photo photo--palette" role="img" aria-label="Photograph of a makeup palette, compact and brushes"></div>
    <div class="photo photo--brush" role="img" aria-label="Photograph of a powder brush"></div>
    <div class="photo photo--powder" role="img" aria-label="Photograph of a face powder pot"></div>
    <div class="wordmark">
      <p class="wordmark__name">Clara Rose</p>
      <p class="wordmark__role">Makeup by</p>
    </div>
  </section>

</main>
</body>
</html>
```